Maren Holt Luxury Wellness Profile Booklet

I am a luxury wellness property agent and would like to create my personal profile booklet. I want this to feel luxurious, minimalist, informative and the philosophy behind wellness and property the cPAGE 1 — THE COVER

Very minimal.

MAREN HOLT

LUXURY WELLNESS PROPERTY

PROPERTY • WELLNESS • LIFESTYLE

Fenwick Dale Coastline Group

Large photograph of you — preferably walking through a beautiful waterfront property or standing naturally within an architectural setting.

At the bottom:

Hope Island • Sanctuary Cove • Helensvale

Small Fenwick Dale logo.

PAGE 2 — THE OPENING STATEMENT

A beautiful full-page lifestyle photograph.

Overlaid:

WHERE PROPERTY
MEETS WELLBEING

“A home is more than an address. It is the environment in which life unfolds.”

Then a short introduction:

Opening Profile

I believe the most exceptional properties are not defined simply by their architecture, address or price.

They are defined by how they make you feel.

Natural light. Water views. Privacy. Green space. Indoor-outdoor living. A place to unwind, entertain, recharge and reconnect.

My approach to luxury property brings these elements together — combining strategic real estate expertise with a genuine understanding of wellness, lifestyle and the way people want to live today.

Because when we understand the lifestyle behind the property, we can create a more compelling story around it.

PAGE 3 — MEET MAREN

Large portrait of you on one side.

Other side:

MEET MAREN

20+ YEARS OF PROPERTY EXPERIENCE

Commercial
Residential
Project Sales
Luxury & Lifestyle Property

Then:

About Maren

With more than 20 years' experience across commercial, residential and project sales, I have built my career around relationships, strategic marketing and delivering exceptional outcomes for my clients.

My approach is warm, considered and highly personal.

I believe sellers deserve more than a listing campaign. They deserve a clear strategy, honest communication and an agent who understands what makes their property valuable — both financially and emotionally.

Today, my focus is luxury lifestyle property across the Northern Gold Coast, with a particular passion for Hope Island, Sanctuary Cove and selected waterfront gated estates in Helensvale.

PAGE 4 — WHY WELLNESS?

This is where your differentiation becomes really powerful.

Full-bleed photograph of:

pool
outdoor entertaining
greenery
water
spa
wellness room
person walking beside water
WELLNESS IS THE NEW LUXURY

Then:

Wellness Philosophy

Luxury has evolved.

Today, luxury is not only about beautiful finishes, expansive living spaces or an impressive address.

It is privacy.

It is waking to water.

It is natural light flooding through the home.

It is having space to breathe.

It is stepping outside into nature, walking along the water, enjoying a morning swim, entertaining beside the pool or creating a private sanctuary at home.

These lifestyle elements increasingly shape the way buyers experience and value a property.

This is where my passion for wellness becomes part of my property approach.

PAGE 5 — MY WELLNESS JOURNEY

This page makes the wellness positioning credible rather than simply being a marketing slogan.

MY WELLNESS JOURNEY

You could use 3 small photographs:

BLOOMTOT CO
SOLACE WELLNESS CENTRE
LUXURY WELLNESS PROPERTY

Copy:

Wellness Journey

My connection with wellness began outside of real estate.

After stepping away from property, I founded Bloomtot Co, developing an organic children's nutritional product with a focus on natural ingredients and wellbeing.

I later launched Solace Wellness Centre, further deepening my understanding of wellness, health-conscious lifestyles and the importance of creating environments that support how we live.

Today, I bring that perspective back into property.

I see homes differently — not simply as buildings, but as environments for living, restoring, entertaining and thriving.

PAGE 6 — THE MAREN HOLT DIFFERENCE

This should be one of your strongest pages.

A DIFFERENT WAY OF SEEING PROPERTY

Use six elegant icons or small images:

01 — LIFESTYLE

I look beyond the floor plan to understand how buyers will actually experience the home.

02 — WELLNESS

I identify the spaces and features that contribute to wellbeing and lifestyle.

03 — PRESENTATION

I create a campaign that makes the property feel aspirational, memorable and emotionally engaging.

04 — STORY

Every exceptional property has a story. I find it, refine it and communicate it.

05 — STRATEGY

From positioning and buyer targeting to campaign execution and negotiation, every element has a purpose.

06 — RELATIONSHIPS

Trust, transparency and communication remain at the centre of every campaign.

PAGE 7 — YOUR PROPERTY STORY

This could be a beautiful editorial spread.

EVERY HOME HAS A STORY

Then:

My role is to discover what makes yours extraordinary.

Three questions:

WHAT MAKES YOUR PROPERTY DIFFERENT?

Architecture?
Waterfront?
Views?
Privacy?
Garden?
Location?

HOW DOES IT MAKE PEOPLE FEEL?

Calm?
Inspired?
Connected?
Entertained?
Relaxed?

WHO WILL FALL IN LOVE WITH IT?

Families?
Executives?
Downsizers?
Boaties?
Golfers?
Wellness-focused buyers?
Lifestyle purchasers?

Then:

I turn these answers into your property's story.

PAGE 8 — YOUR NORTHERN GOLD COAST

Beautiful aerial/waterfront image.

MY MARKET

HOPE ISLAND

SANCTUARY COVE

HELENSVALE

WATERFRONT & GATED ESTATES

Copy:

Northern Gold Coast

I specialise in the lifestyle-driven property market of the Northern Gold Coast.

From the waterfront homes and private enclaves of Hope Island and Sanctuary Cove to the established gated estates of Helensvale, I understand the lifestyle characteristics that attract buyers to this part of the Gold Coast.

Having personally experienced the lifestyle of these communities, I understand that buyers are often purchasing far more than a house.

They are buying a way of life.

PAGE 9 — THE WELLNESS PROPERTY

This could become your signature page.

WHAT MAKES A WELLNESS HOME?

Use a sophisticated grid:

WATER
Pools • Waterfront • Marina • Water views

NATURE
Green space • Gardens • Reserve outlooks • Walking trails

LIGHT
Natural light • Orientation • Open spaces

MOVEMENT
Walking • Golf • Boating • Outdoor living

RESTORATION
Spa • Sauna • Cold plunge • Retreat spaces

CONNECTION
Entertaining • Family • Indoor/outdoor living

Bottom:

The most desirable luxury is often the way a home makes you feel.

PAGE 10 — THE SELLING EXPERIENCE
YOUR HOME. YOUR STORY. YOUR CAMPAIGN.

I would make this a simple six-stage journey:

01 — DISCOVER
Understand your property, your goals and your lifestyle.

↓

02 — POSITION
Establish the property's unique market position.

↓

03 — PREPARE
Presentation, styling and strategic recommendations.

↓

04 — CREATE
Photography, film, editorial storytelling and digital marketing.

↓

05 — CONNECT
Targeted buyer engagement and database activation.

↓

06 — NEGOTIATE
Strategic negotiation designed to maximise the opportunity.

PAGE 11 — THE POWER OF PRESENTATION

Large before/after style photography.

FIRST IMPRESSIONS ARE EVERYTHING

Copy:

We don't get a second opportunity to create a first impression.

Then explain your approach to:

styling
photography
cinematic video
twilight imagery
aerial photography
lifestyle storytelling
digital advertising
targeted database marketing
buyer follow-up
auction strategy

Importantly, don't make this page feel like a generic list of marketing products.

Frame everything around:

Creating desire before creating urgency.
PAGE 12 — PROVEN RESULTS

Now introduce your actual results.

RESULTS THAT BUILD CONFIDENCE

Use your strongest results as elegant case studies.

For example:
4183 Palmetto Drive, Hope Island
$3,850,000
34 Days On The Market

$2.90M
71 Heron Bay Boulevard, Helensvale
Sold within 45 days

Include your result and the property's story.

$2.15M

3/9 Heron Bay Boulevard

Waterfront Villa

Then potentially:

28 DAYS

5419 Quaywood Boulevard, Hope Island

Under contract following relaunch

If a result subsequently changed because the contract fell through, be careful about how you describe the current status. We can make this page completely accurate to the final outcome.

PAGE 13 — THE FENWICK DALE ADVANTAGE

This is where you let the brand support you, rather than letting the booklet become a Fenwick Dale corporate brochure.

PERSONAL SERVICE.
NATIONAL REACH.

Then a short statement about your Fenwick Dale platform.

You could include:

POWERFUL BUYER DATABASE

LUXURY PROPERTY MARKETING

AUCTION EXPERTISE

DIGITAL REACH

LOCAL KNOWLEDGE

NATIONAL NETWORK

And a short line:

The personal attention of a specialist agent, supported by the strength of a globally recognised property network.

PAGE 14 — WHAT YOU CAN EXPECT FROM ME

This page is very important for your seller proposition.

MY PROMISE TO YOU

TRANSPARENCY

Clear advice, honest feedback and no unnecessary promises.

COMMUNICATION

You will know what is happening throughout your campaign.

STRATEGY

Every decision is made with your property, market and objectives in mind.

ATTENTION TO DETAIL

Your home deserves meticulous preparation and presentation.

PERSONAL SERVICE

You deal directly with me throughout your campaign.

RESULT FOCUS

My role is to create the strongest possible environment for a successful sale.

PAGE 15 — THE CLOSING PAGE

This should be very luxurious and emotional.

Beautiful photograph of water at sunset / luxury pool / Hope Island lifestyle.

YOUR HOME.
YOUR NEXT CHAPTER.

Then:

Closing Statement

Selling a home is rarely just a transaction.

It is the closing of one chapter and the beginning of another.

My role is to make the journey feel considered, strategic and personal — while creating the strongest possible opportunity for your property in the marketplace.

Thank you for considering me to represent your home.

I would be honoured to tell its story.

Then your details:

MAREN HOLT

Luxury Wellness Property

0412 557 830

BACK COVER

Keep it extremely clean.

Your photograph or perhaps a beautiful Gold Coast waterfront image.

MAREN HOLT

LUXURY WELLNESS PROPERTY

0412 557 830

Fenwick Dale logoollaboration. I can send a full brief if required.

Target Market(s)

Luxury Property Owners

Industry/Entity Type

Wellness Luxury Real Estate Lifestyle

Requirements
Must have
• A luxurious minimalist clean feel

```html
<!DOCTYPE html>
<html lang="en">
<head>
<meta charset="utf-8">
<title>Maren Holt — Luxury Wellness Profile Booklet</title>
<link rel="stylesheet" href="https://fonts.googleapis.com/css2?family=Archivo:wght@400;500;600;700&family=Inter:wght@400;500;600&family=Cormorant+Garamond:ital,wght@1,400&family=Oswald:wght@400;500&display=swap">
<style>
:root{
  --cream:#f3efe7;
  --cream-deep:#ebe5da;
  --charcoal:#24282a;
  --ink:#2a2a2a;
  --muted:#8a8580;
  --gold:#b99455;
  --gold-soft:#cdb07a;
  --white:#ffffff;
  --line:#d8d1c4;
  --canvas:#ffffff;
}
*{box-sizing:border-box;margin:0;padding:0}
html,body{width:1200px;height:2686px;overflow:hidden;background:var(--canvas)}
body{position:relative;font-family:"Inter",Arial,sans-serif;color:var(--ink)}
.page{position:absolute;width:352px;height:497px;overflow:hidden;background:var(--cream)}
.page.dark{background:var(--charcoal);color:var(--white)}
.col-1{left:43px}.col-2{left:414px}.col-3{left:786px}
.row-1{top:38px}.row-2{top:555px}.row-3{top:1073px}.row-4{top:1592px;height:491px}.row-5{top:2105px;height:494px}

.photo{position:absolute}
.headline{font-family:"Archivo",Arial,sans-serif;font-weight:600;font-size:14px;line-height:1.22;letter-spacing:.4px;text-transform:uppercase;color:var(--ink)}
.headline.light{color:var(--white)}
.eyebrow{font-family:"Archivo",Arial,sans-serif;font-size:4.2px;font-weight:600;letter-spacing:.5px;text-transform:uppercase;color:var(--gold)}
.body-copy p{font-size:4.6px;line-height:1.6;margin-bottom:4px;color:#3d3a37}
.script{font-family:"Cormorant Garamond",Georgia,serif;font-style:italic;font-size:7px;color:#6f6a64}
.footer{position:absolute;left:24px;right:24px;bottom:10px;display:flex;justify-content:space-between;font-family:"Archivo",Arial,sans-serif;font-size:3.6px;letter-spacing:.4px;text-transform:uppercase;color:var(--muted)}
.dark .footer{color:#9a9a95}
.content{position:absolute;left:24px;right:24px}

/* cover */
.cover-photo{inset:0;background:linear-gradient(180deg,#e9e7e4 0%,#cfcac4 28%,#1c1f22 48%,#2b2a28 60%,#3b9a8c 74%,#235e58 86%,#1d1f20 100%)}
.cover-shade{position:absolute;inset:0;background:linear-gradient(180deg,rgba(0,0,0,.35) 0%,rgba(0,0,0,0) 30%,rgba(0,0,0,0) 80%,rgba(0,0,0,.45) 100%)}
.cover-title{top:38px}
.cover-sub{font-size:5.5px;color:#f1f1f1;letter-spacing:.4px;margin-top:10px}
.cover-tag{font-size:4px;color:var(--gold-soft);font-weight:600;letter-spacing:.4px;margin-top:8px;font-family:"Archivo",Arial,sans-serif}
.cover-foot{bottom:22px;color:var(--white)}
.cover-foot .brand{font-family:"Archivo",Arial,sans-serif;font-size:4.2px;font-weight:600;letter-spacing:.3px}
.cover-foot .places{font-size:3.8px;margin-top:4px;color:#ddd}

/* opening */
.sunset{inset:0;background:linear-gradient(180deg,#5e6a70 0%,#8c8a82 18%,#d49a55 34%,#7a5a35 46%,#3a3d2b 56%,#55614f 66%,#274550 80%,#1f3c4a 100%)}
.card{position:absolute;background:rgba(255,255,255,.96);border-radius:6px;padding:10px 12px}
.card .eyebrow{margin-bottom:6px}
.card p{font-size:4.2px;line-height:1.55;margin-bottom:5px;color:#3d3a37}

/* meet */
.portrait{left:0;top:0;width:165px;height:100%;background:linear-gradient(180deg,#e9e5de 0%,#ddd6cb 40%,#efe9df 70%,#d7cdbf 100%)}
.meet-text{left:187px;right:22px;top:38px}
.meet-text .headline{font-size:9.6px;margin-top:5px}
.meet-list{margin-top:12px}
.meet-list li{list-style:none;font-size:4.4px;color:#77716a;margin-bottom:6px}
.rule{height:1px;background:var(--line);margin:10px 0}

/* wellness */
.house{inset:0;background:linear-gradient(180deg,#2f5d93 0%,#4c7bb1 20%,#e8e8e6 36%,#d7d6d3 52%,#5b5d60 62%,#2f8bb1 74%,#1e5c7d 84%,#3b3d3f 100%)}

/* journey */
.trio{display:flex;gap:7px;margin-top:20px}
.trio figure{flex:1;position:relative;height:86px}
.trio .photo{position:absolute;inset:0}
.trio figcaption{position:absolute;left:0;right:0;bottom:0;height:12px;background:rgba(60,60,60,.55);color:#fff;font-size:3.4px;font-weight:600;letter-spacing:.3px;padding:4px 4px;font-family:"Archivo",Arial,sans-serif}

/* difference */
.diff-grid{display:grid;grid-template-columns:repeat(3,1fr);gap:8px;margin-top:22px}
.diff-card{height:161px;border:1px solid var(--gold);border-radius:10px;text-align:center;padding:16px 8px 0}
.diff-card svg{width:34px;height:34px;stroke:var(--gold);fill:none;stroke-width:1.2}
.diff-card h3{font-family:"Archivo",Arial,sans-serif;font-weight:500;font-size:8px;letter-spacing:.3px;margin:22px 0 6px}
.diff-card p{font-size:5.2px;line-height:1.25;color:#eee}

/* story */
.q-cols{display:grid;grid-template-columns:1fr 1fr 1fr;gap:6px;margin-top:26px}
.q-cols h4{font-family:"Archivo",Arial,sans-serif;font-size:3.9px;font-weight:600;letter-spacing:.2px;margin-bottom:7px}
.q-cols li{list-style:none;font-size:4.3px;color:#7b756f;margin-bottom:5.5px}

/* market */
.market-photo{left:167px;top:0;right:0;bottom:0;background:linear-gradient(180deg,#3c7fc4 0%,#6aa3d6 18%,#4d7a3c 32%,#3f6a31 50%,#70756e 64%,#d8d6d2 76%,#6a7c48 92%,#3d5a2b 100%)}
.market-text{left:24px;width:128px;top:34px}
.areas li{list-style:none;font-family:"Archivo",Arial,sans-serif;font-size:4.4px;font-weight:500;color:#77716a;margin-bottom:7px;letter-spacing:.3px}

/* wellness home */
.canal{left:0;top:0;right:0;height:225px;background:linear-gradient(180deg,#6b7f8f 0%,#c2a98a 20%,#3c5a32 38%,#4f6b3b 52%,#8ab8c9 66%,#5f98b3 82%,#c7c3bb 100%)}
.wh-grid{display:grid;grid-template-columns:1fr 1fr;row-gap:26px;column-gap:20px;top:254px}
.wh-grid h4{font-family:"Archivo",Arial,sans-serif;font-size:4.8px;font-weight:500;color:#77716a;letter-spacing:.3px;margin-bottom:6px}
.wh-grid p{font-size:3.8px;color:#77716a}

/* stages */
.journey-art{left:115px;top:118px;width:112px;height:256px;border-radius:28px;background:linear-gradient(180deg,#c9ab75 0%,#ddd7cb 20%,#c9ab75 40%,#ddd7cb 60%,#c9ab75 80%,#ddd7cb 100%)}
.stage-pill{position:absolute;height:14px;width:48px;border-radius:7px;background:#e7e2d8;border:.6px solid var(--ink);font-family:"Oswald",Arial,sans-serif;font-size:6.5px;line-height:13px;text-align:center;color:var(--ink)}
.stage-lead{position:absolute;height:0;border-top:1.2px dotted var(--ink)}
.stage-box{position:absolute;width:74px;background:var(--white);border:.7px solid var(--ink);border-radius:5px;padding:5px 7px}
.stage-box h3{font-family:"Oswald",Arial,sans-serif;font-weight:400;font-size:9px;color:var(--gold);line-height:1.1}
.stage-box p{font-family:"Cormorant Garamond",Georgia,serif;font-size:4.4px;line-height:1.2;color:#3d3a37;margin-top:3px}

/* presentation */
.pair{display:flex;gap:7px;margin-top:30px;height:128px}
.pair figure{flex:1;position:relative}
.pair .photo{inset:0}
.pair figcaption{position:absolute;left:0;bottom:0;right:0;height:11px;background:rgba(70,70,70,.45);color:#fff;font-size:3.3px;padding:4px 4px;font-family:"Archivo",Arial,sans-serif}
.bullets{display:grid;grid-template-columns:1fr 1fr;gap:0 10px;margin-top:18px}
.bullets li{font-size:4.2px;color:#3d3a37;margin:0 0 6px 7px}

/* results */
.results{display:grid;grid-template-columns:repeat(3,1fr);gap:6px;margin-top:40px}
.results .photo{position:relative;height:198px}
.stat{font-family:"Archivo",Arial,sans-serif;font-weight:700;font-size:14px;color:var(--gold);margin-top:10px}
.addr{font-size:4.6px;color:#3d3a37;line-height:1.3;margin-top:2px}
.status{border-left:1px solid var(--gold);padding-left:5px;margin-top:9px;font-family:"Archivo",Arial,sans-serif;font-size:6.5px;font-weight:600;color:var(--gold);line-height:1.2}
.note{font-size:3.8px;color:#3d3a37;margin-top:24px;line-height:1.4}

/* advantage */
.adv-grid{display:grid;grid-template-columns:1fr 1fr;gap:0 10px;margin-top:36px}
.adv-grid div{font-family:"Archivo",Arial,sans-serif;font-size:4.4px;font-weight:600;letter-spacing:.2px;padding-bottom:5px;border-bottom:1px solid #4b4f50;margin-bottom:34px}

/* promise */
.promise-grid{display:grid;grid-template-columns:1fr 1fr;gap:0 14px;margin-top:28px}
.promise-grid section{min-height:62px}
.promise-grid h4{font-family:"Archivo",Arial,sans-serif;font-size:4.6px;font-weight:500;letter-spacing:.3px;color:#77716a;margin-bottom:7px}
.promise-grid p{font-size:4.2px;color:#3d3a37;line-height:1.5}

/* closing */
.close-card{position:absolute;left:24px;right:24px;top:304px;height:170px;background:rgba(35,38,40,.72);border-radius:6px;padding:12px 14px;color:#fff}
.close-card p{font-size:4.2px;line-height:1.55;margin-bottom:5px;color:#eee}
.contact{display:flex;justify-content:space-between;align-items:flex-end;margin-top:18px}
.contact .name{font-family:"Archivo",Arial,sans-serif;font-size:5px;font-weight:600}
.contact small{display:block;font-size:3.6px;color:#ddd;margin-top:2px}
</style>
</head>
<body>

<!-- 01 Cover -->
<article class="page col-1 row-1">
  <div class="photo cover-photo" role="img" aria-label="Architectural kitchen with arched alcove, sculptural pendant and teal velvet bar stools"></div>
  <div class="cover-shade"></div>
  <div class="content cover-title">
    <h1 class="headline light">Maren Holt</h1>
    <p class="cover-sub">LUXURY WELLNESS PROPERTY</p>
    <p class="cover-tag">PROPERTY • WELLNESS • LIFESTYLE</p>
  </div>
  <div class="content cover-foot">
    <p class="brand">FENWICK DALE COASTLINE GROUP</p>
    <p class="places">Hope Island • Sanctuary Cove • Helensvale</p>
  </div>
</article>

<!-- 02 Opening -->
<article class="page col-2 row-1">
  <div class="photo sunset" role="img" aria-label="Waterfront sunset over canal with pool and glass balustrade"></div>
  <div class="content" style="top:46px">
    <h2 class="headline light">Where property<br>meets wellbeing</h2>
    <p class="script" style="color:#eee;font-size:5.6px;margin-top:12px">“A home is more than an address. It is the environment in which life unfolds.”</p>
  </div>
  <div class="card" style="left:24px;right:24px;top:352px;height:114px">
    <p class="eyebrow">Opening Profile</p>
    <p>I believe the most exceptional properties are not defined simply by their architecture, address or price.</p>
    <p>They are defined by how they make you feel.</p>
    <p>Natural light. Water views. Privacy. Green space. Indoor-outdoor living. A place to unwind, entertain, recharge and reconnect.</p>
    <p>My approach to luxury property brings these elements together — combining strategic real estate expertise with a genuine understanding of wellness, lifestyle and the way people want to live today.</p>
    <p>Because when we understand the lifestyle behind the property, we can create a more compelling story around it.</p>
  </div>
  <div class="footer" style="color:#c9c9c9"><span>Maren Holt / Luxury Wellness Property</span><span>02</span></div>
</article>

<!-- 03 Meet -->
<article class="page col-3 row-1">
  <div class="photo portrait" role="img" aria-label="Portrait of Maren seated in a light interior, dressed in cream"></div>
  <div class="content meet-text">
    <p class="eyebrow">Meet Maren</p>
    <h2 class="headline">20+ years of<br>property experience</h2>
    <ul class="meet-list"><li>Commercial</li><li>Residential</li><li>Project Sales</li><li>Luxury &amp; Lifestyle Property</li></ul>
    <div class="rule"></div>
    <p class="eyebrow" style="margin-bottom:10px">About Maren</p>
    <div class="body-copy">
      <p>With more than 20 years' experience across commercial, residential and project sales, I have built my career around relationships, strategic marketing and delivering exceptional outcomes for my clients.</p>
      <p>My approach is warm, considered and highly personal.</p>
      <p>I believe sellers deserve more than a listing campaign. They deserve a clear strategy, honest communication and an agent who understands what makes their property valuable — both financially and emotionally.</p>
      <p>Today, my focus is luxury lifestyle property across the Northern Gold Coast, with a particular passion for Hope Island, Sanctuary Cove and selected waterfront gated estates in Helensvale.</p>
    </div>
  </div>
  <div class="footer" style="left:187px"><span>Maren Holt / Luxury Wellness Property</span><span>03</span></div>
</article>

<!-- 04 Wellness -->
<article class="page col-1 row-2">
  <div class="photo house" role="img" aria-label="Modern white home at dusk with stone feature wall and pool"></div>
  <div class="content" style="top:40px">
    <h2 class="headline light">Wellness is<br>the new luxury</h2>
  </div>
  <div class="card" style="left:26px;right:26px;top:318px;height:148px">
    <p class="eyebrow">Wellness Philosophy</p>
    <p>Luxury has evolved.</p>
    <p>Today, luxury is not only about beautiful finishes, expansive living spaces or an impressive address.</p>
    <p style="margin-bottom:1px">It is privacy.</p>
    <p style="margin-bottom:1px">It is waking to water.</p>
    <p style="margin-bottom:1px">It is natural light flooding through the home.</p>
    <p>It is having space to breathe.</p>
    <p>It is stepping outside into nature, walking along the water, enjoying a morning swim, entertaining beside the pool or creating a private sanctuary at home.</p>
    <p>These lifestyle elements increasingly shape the way buyers experience and value a property.</p>
    <p>This is where my passion for wellness becomes part of my property approach.</p>
  </div>
  <div class="footer" style="color:#ccc"><span></span><span>04</span></div>
</article>

<!-- 05 Journey -->
<article class="page col-2 row-2">
  <div class="content" style="top:32px">
    <p class="eyebrow">My Wellness Journey</p>
    <h2 class="headline" style="margin-top:6px">A perspective<br>built outside real estate</h2>
    <div class="trio">
      <figure><div class="photo" style="background:linear-gradient(180deg,#f1ede7,#dcd4c9)" role="img" aria-label="Maren in a bright white studio"></div><figcaption>BLOOMTOT CO</figcaption></figure>
      <figure><div class="photo" style="background:linear-gradient(180deg,#ece6dd,#cfc5b8)" role="img" aria-label="Maren seated in a calm wellness interior"></div><figcaption>SOLACE WELLNESS CENTRE</figcaption></figure>
      <figure><div class="photo" style="background:linear-gradient(180deg,#7e8b93,#d49a55 45%,#3f4a34 70%,#2f5060)" role="img" aria-label="Canal-front pool at sunset"></div><figcaption>LUXURY WELLNESS PROPERTY</figcaption></figure>
    </div>
    <div class="body-copy" style="margin-top:16px">
      <p>My connection with wellness began outside of real estate.</p>
      <p>After stepping away from property, I founded Bloomtot Co, developing an organic children's nutritional product with a focus on natural ingredients and wellbeing.</p>
      <p>I later launched Solace Wellness Centre, further deepening my understanding of wellness, health-conscious lifestyles and the importance of creating environments that support how we live.</p>
      <p>Today, I bring that perspective back into property.</p>
      <p>I see homes differently — not simply as buildings, but as environments for living, restoring, entertaining and thriving.</p>
    </div>
  </div>
  <div class="footer"><span>Maren Holt / Luxury Wellness Property</span><span>05</span></div>
</article>

<!-- 06 Difference -->
<article class="page dark col-3 row-2">
  <div class="content" style="top:30px">
    <h2 class="headline light" style="font-size:11px">A different way of seeing property</h2>
    <p class="eyebrow" style="margin-top:6px">The Maren Holt Difference</p>
    <div class="diff-grid">
      <div class="diff-card"><svg viewBox="0 0 34 34"><circle cx="12" cy="10" r="4"/><path d="M5 26c0-5 3-8 7-8s7 3 7 8z"/><circle cx="25" cy="9" r="4"/><path d="M25 7v4M23 9h4"/><rect x="19" y="20" width="10" height="8"/></svg><h3>LIFESTYLE</h3><p>I look beyond the floor plan to understand how buyers will actually experience the home.</p></div>
      <div class="diff-card"><svg viewBox="0 0 34 34"><circle cx="17" cy="9" r="3"/><path d="M17 13c-4 2-8 2-10 1M17 13c4 2 8 2 10 1M17 14v8M10 27c3-6 11-6 14 0M6 22c4 0 7 2 11 6M28 22c-4 0-7 2-11 6M17 2v2M10 4l1 2M24 4l-1 2"/></svg><h3>WELLNESS</h3><p>I identify the spaces and features that contribute to wellbeing and lifestyle.</p></div>
      <div class="diff-card"><svg viewBox="0 0 34 34"><rect x="9" y="5" width="21" height="15"/><path d="M13 16l4-5 3 3 5-6M19 20v6M15 30l4-4 4 4"/><circle cx="5" cy="12" r="2.5"/><path d="M2 24c0-4 1.5-7 3-7s3 3 3 7"/></svg><h3>PRESENTATION</h3><p>I create a campaign that makes the property feel aspirational, memorable and emotionally engaging.</p></div>
      <div class="diff-card"><svg viewBox="0 0 34 34"><path d="M8 5h18v24H8z"/><path d="M12 11h10M12 15h10M12 19h7"/><path d="M24 24l6-8 2 2-6 8-3 1z"/></svg><h3>STORY</h3><p>Every exceptional property has a story. I find it, refine it and communicate it.</p></div>
      <div class="diff-card"><svg viewBox="0 0 34 34"><circle cx="17" cy="16" r="9"/><circle cx="17" cy="16" r="4"/><path d="M17 3v4M17 25v4M4 16h4M26 16h4M8 7l3 3M26 7l-3 3M8 25l3-3M26 25l-3-3"/></svg><h3>STRATEGY</h3><p>From positioning and buyer targeting to campaign execution and negotiation, every element has a purpose.</p></div>
      <div class="diff-card"><svg viewBox="0 0 34 34"><path d="M17 29L5 17a6 6 0 0 1 12-7 6 6 0 0 1 12 7z"/><path d="M10 18l5-4 4 3 4-3"/></svg><h3>RELATIONSHIPS</h3><p>Trust, transparency and communication remain at the centre of every campaign.</p></div>
    </div>
  </div>
  <div class="footer"><span>Maren Holt / Luxury Wellness Property</span><span></span></div>
</article>

<!-- 07 Story -->
<article class="page col-1 row-3">
  <div class="content" style="top:30px">
    <p class="eyebrow">Your Property Story</p>
    <h2 class="headline" style="margin-top:6px">Every home<br>has a story</h2>
    <p class="script" style="font-size:5.6px;margin-top:8px">My role is to discover what makes yours extraordinary.</p>
    <div class="q-cols">
      <div><h4>WHAT MAKES YOUR PROPERTY DIFFERENT?</h4><ul><li>Architecture?</li><li>Waterfront?</li><li>Views?</li><li>Privacy?</li><li>Garden?</li><li>Location?</li></ul></div>
      <div><h4>HOW DOES IT MAKE PEOPLE FEEL?</h4><ul><li>Calm?</li><li>Inspired?</li><li>Connected?</li><li>Entertained?</li><li>Relaxed?</li></ul></div>
      <div><h4>WHO WILL FALL IN LOVE WITH IT?</h4><ul><li>Families?</li><li>Executives?</li><li>Downsizers?</li><li>Boaties?</li><li>Golfers?</li><li>Wellness-focused buyers?</li><li>Lifestyle purchasers?</li></ul></div>
    </div>
  </div>
  <p class="script content" style="top:446px">I turn these answers into your property's story.</p>
  <div class="footer"><span>Maren Holt / Luxury Wellness Property</span><span>07</span></div>
</article>

<!-- 08 Market -->
<article class="page col-2 row-3">
  <div class="photo market-photo" role="img" aria-label="Waterfront garden with moored cruiser and fire pit"></div>
  <div class="content market-text">
    <p class="eyebrow">Your Northern Gold Coast</p>
    <h2 class="headline" style="margin-top:8px">My market</h2>
    <ul class="areas" style="margin-top:14px"><li>HOPE ISLAND</li><li>SANCTUARY COVE</li><li>HELENSVALE</li><li>WATERFRONT &amp; GATED ESTATES</li></ul>
    <div class="rule" style="margin:16px 0 10px"></div>
    <p class="eyebrow" style="margin-bottom:10px">Northern Gold Coast</p>
    <div class="body-copy">
      <p>I specialise in the lifestyle-driven property market of the Northern Gold Coast.</p>
      <p>From the waterfront homes and private enclaves of Hope Island and Sanctuary Cove to the established gated estates of Helensvale, I understand the lifestyle characteristics that attract buyers to this part of the Gold Coast.</p>
      <p>Having personally experienced the lifestyle of these communities, I understand that buyers are often purchasing far more than a house.</p>
      <p>They are buying a way of life.</p>
    </div>
  </div>
  <div class="footer" style="right:200px"><span>Maren Holt / Luxury Wellness Property</span></div>
</article>

<!-- 09 Wellness home -->
<article class="page col-3 row-3" style="background:var(--cream-deep)">
  <div class="photo canal" role="img" aria-label="Canal-front pool with moored cruisers at sunset"></div>
  <h2 class="headline light content" style="top:30px;font-size:11.5px">What makes a wellness home?</h2>
  <div class="content wh-grid">
    <div><h4>WATER</h4><p>Pools • Waterfront • Marina • Water views</p></div>
    <div><h4>NATURE</h4><p>Green space • Gardens • Reserve outlooks • Walking trails</p></div>
    <div><h4>LIGHT</h4><p>Natural light • Orientation • Open spaces</p></div>
    <div><h4>MOVEMENT</h4><p>Walking • Golf • Boating • Outdoor living</p></div>
    <div><h4>RESTORATION</h4><p>Spa • Sauna • Cold plunge • Retreat spaces</p></div>
    <div><h4>CONNECTION</h4><p>Entertaining • Family • Indoor/outdoor living</p></div>
  </div>
  <p class="script content" style="top:456px;font-size:6px">The most desirable luxury is often the way a home makes you feel.</p>
  <div class="footer"><span>Maren Holt / Luxury Wellness Property</span><span>09</span></div>
</article>

<!-- 10 Stages -->
<article class="page col-1 row-4">
  <div class="content" style="top:30px">
    <p class="eyebrow">The Selling Experience</p>
    <h2 class="headline" style="margin-top:6px">Your home. Your story.<br>Your campaign.</h2>
  </div>
  <div class="photo journey-art" role="img" aria-label="Winding gold and stone journey path illustration linking six stages"></div>

  <div class="stage-box" style="left:24px;top:98px"><h3>DISCOVER</h3><p>Understand your property, your goals and your lifestyle.</p></div>
  <div class="stage-box" style="left:252px;top:153px"><h3>POSITION</h3><p>Establish the property's unique market position.</p></div>
  <div class="stage-box" style="left:24px;top:200px"><h3>PREPARE</h3><p>Presentation, styling and strategic recommendations.</p></div>
  <div class="stage-box" style="left:252px;top:242px"><h3>CREATE</h3><p>Photography, film, editorial storytelling and digital marketing.</p></div>
  <div class="stage-box" style="left:24px;top:286px"><h3>CONNECT</h3><p>Targeted buyer engagement and database activation.</p></div>
  <div class="stage-box" style="left:252px;top:330px"><h3>NEGOTIATE</h3><p>Strategic negotiation designed to maximise the opportunity.</p></div>

  <div class="stage-lead" style="left:106px;width:46px;top:143px"></div>
  <div class="stage-lead" style="left:204px;width:46px;top:181px"></div>
  <div class="stage-lead" style="left:106px;width:46px;top:220px"></div>
  <div class="stage-lead" style="left:204px;width:46px;top:259px"></div>
  <div class="stage-lead" style="left:106px;width:46px;top:298px"></div>
  <div class="stage-lead" style="left:204px;width:46px;top:337px"></div>

  <div class="stage-pill" style="left:154px;top:136px">STAGE 01</div>
  <div class="stage-pill" style="left:154px;top:174px">STAGE 02</div>
  <div class="stage-pill" style="left:154px;top:213px">STAGE 03</div>
  <div class="stage-pill" style="left:154px;top:252px">STAGE 04</div>
  <div class="stage-pill" style="left:154px;top:291px">STAGE 05</div>
  <div class="stage-pill" style="left:154px;top:330px">STAGE 06</div>
  <div class="footer"><span>Maren Holt / Luxury Wellness Property</span><span>10</span></div>
</article>

<!-- 11 Presentation -->
<article class="page col-2 row-4" style="width:347px">
  <div class="content" style="top:30px">
    <p class="eyebrow">The Power of Presentation</p>
    <h2 class="headline" style="margin-top:6px">First impressions<br>are everything</h2>
    <div class="pair">
      <figure><div class="photo" style="background:linear-gradient(180deg,#e6e4e1,#1f2224 45%,#3a9a8a 75%,#222 100%)" role="img" aria-label="Styled kitchen with arched alcove and teal stools"></div><figcaption>PROPERTY PRESENCE</figcaption></figure>
      <figure><div class="photo" style="background:linear-gradient(180deg,#f4f2ef,#e3ddd4)" role="img" aria-label="Maren laughing in a bright white living room"></div><figcaption>LIFESTYLE STORY</figcaption></figure>
    </div>
    <p class="script" style="font-size:5.4px;margin-top:10px">We don't get a second opportunity to create a first impression.</p>
    <div class="bullets">
      <ul><li>styling</li><li>photography</li><li>cinematic video</li><li>twilight imagery</li><li>aerial photography</li></ul>
      <ul><li>lifestyle storytelling</li><li>digital advertising</li><li>targeted database marketing</li><li>buyer follow-up</li><li>auction strategy</li></ul>
    </div>
  </div>
  <p class="script content" style="top:446px;font-size:6px">Creating desire before creating urgency.</p>
  <div class="footer"><span>Maren Holt / Luxury Wellness Property</span><span>11</span></div>
</article>

<!-- 12 Results -->
<article class="page col-3 row-4" style="width:348px">
  <div class="content" style="top:30px">
    <p class="eyebrow">Proven Results</p>
    <h2 class="headline" style="margin-top:6px">Results that build<br>confidence</h2>
    <div class="results">
      <div><div class="photo" style="background:linear-gradient(180deg,#e6e4e1,#1f2224 45%,#3a9a8a 75%,#222)" role="img" aria-label="Kitchen interior with arched alcove"></div>
        <p class="stat">$2.90M</p><p class="addr">71 Heron Bay Boulevard,<br>Helensvale</p><p class="status">Sold within<br>45 days</p></div>
      <div><div class="photo" style="background:linear-gradient(180deg,#3d6fa8,#e7e6e3 35%,#4f5255 60%,#2f8bb1 80%,#ccc)" role="img" aria-label="White villa with pool"></div>
        <p class="stat">$2.15M</p><p class="addr">3/9 Heron Bay Boulevard</p><p class="status">Waterfront<br>Villa</p></div>
      <div><div class="photo" style="background:linear-gradient(180deg,#5c8fc4,#3f6a31 35%,#dcdcdc 62%,#4a4d4f 85%,#6b7a48)" role="img" aria-label="Waterfront garden with moored cruiser"></div>
        <p class="stat">28 DAYS</p><p class="addr">5419 Quaywood Boulevard,<br>Hope Island</p><p class="status">Waterfront<br>Villa</p></div>
    </div>
    <p class="note">If a result subsequently changed because the contract fell through, be careful about how you describe the current status. We can make this page completely accurate to the final outcome.</p>
  </div>
  <div class="footer"><span>Maren Holt / Luxury Wellness Property</span><span>12</span></div>
</article>

<!-- 13 Advantage -->
<article class="page dark col-1 row-5" style="width:348px">
  <div class="content" style="top:32px">
    <h2 class="headline light">Personal service.<br><span style="color:var(--gold)">National reach.</span></h2>
    <p class="eyebrow" style="margin-top:8px">Fenwick Dale Advantage</p>
    <div class="adv-grid">
      <div>POWERFUL BUYER DATABASE</div><div>LUXURY PROPERTY MARKETING</div>
      <div>AUCTION EXPERTISE</div><div>DIGITAL REACH</div>
      <div>LOCAL KNOWLEDGE</div><div>NATIONAL NETWORK</div>
    </div>
  </div>
  <p class="script content" style="top:398px;color:#ddd;font-size:6px">The personal attention of a specialist agent, supported by the strength of a globally recognised property network.</p>
  <p class="eyebrow content" style="top:444px">Fenwick Dale / Coastline Group</p>
  <div class="rule" style="position:absolute;left:24px;right:24px;top:458px;background:#4b4f50;margin:0"></div>
  <div class="footer"><span>Maren Holt / Luxury Wellness Property</span><span></span></div>
</article>

<!-- 14 Promise -->
<article class="page col-2 row-5" style="left:418px;width:342px">
  <div class="content" style="top:30px">
    <p class="eyebrow">What You Can Expect From Me</p>
    <h2 class="headline" style="margin-top:6px">My promise<br>to you</h2>
    <div class="promise-grid">
      <section><h4>TRANSPARENCY</h4><p>Clear advice, honest feedback and no unnecessary promises.</p></section>
      <section><h4>COMMUNICATION</h4><p>You will know what is happening throughout your campaign.</p></section>
      <section><h4>STRATEGY</h4><p>Every decision is made with your property, market and objectives in mind.</p></section>
      <section><h4>ATTENTION TO DETAIL</h4><p>Your home deserves meticulous preparation and presentation.</p></section>
      <section><h4>PERSONAL SERVICE</h4><p>You deal directly with me throughout your campaign.</p></section>
      <section><h4>RESULT FOCUS</h4><p>My role is to create the strongest possible environment for a successful sale.</p></section>
    </div>
  </div>
  <div class="footer"><span>Maren Holt / Luxury Wellness Property</span><span>14</span></div>
</article>

<!-- 15 Closing -->
<article class="page col-3 row-5" style="left:790px;width:350px">
  <div class="photo sunset" role="img" aria-label="Sunset over waterfront pool and canal with trees"></div>
  <div class="content" style="top:32px">
    <h2 class="headline light">Your home.<br>Your next chapter.</h2>
  </div>
  <div class="close-card">
    <p class="eyebrow" style="margin-bottom:8px">Closing Statement</p>
    <p>Selling a home is rarely just a transaction.</p>
    <p>It is the closing of one chapter and the beginning of another.</p>
    <p>My role is to make the journey feel considered, strategic and personal — while creating the strongest possible opportunity for your property in the marketplace.</p>
    <p style="margin-bottom:1px">Thank you for considering me to represent your home.</p>
    <p>I would be honoured to tell its story.</p>
    <div class="contact">
      <div><p class="name">MAREN HOLT</p><small>Luxury Wellness Property</small><small>Fenwick Dale Coastline Group</small></div>
      <div style="text-align:right"><p class="name">0412 557 830</p><small>Hope Island • Sanctuary Cove • Helensvale</small></div>
    </div>
  </div>
</article>

</body>
</html>
```